Holiday Promo Vexo Ad design for culinary tourism company

We need a new design with different Vexo Ad versions for our holiday promotions.
9 graphics needed - with 2 sizes for each one.

DESIGN NOTES
Style: See our website www.pantryalleyways.example for our style of brand visuals and images. These are holiday promos to entice customers to learn more about us and buy our services.

Two images are attached as reference. Harbor Skillet is a previous Vexo ad that we published. We want our holiday promo to be brighter like our website and with your creativity.

The 2nd reference image (Trip Specific) shows how we want there to be different design elements for the copy (the tagline, the body copy, and the buttons/boxes that highlight the 15% off and Use code). It does not have to be a button/box - we just want it to stand out.

Mood: inspiring, upbeat, curious, in-the-know, expert, friendly, authentic

1. ETA (All Vexo graphics in 2 sizes: 1:1 and 9:16)

* General Dark Ad Carousel:
* 1 Graphic promoting 15% Off Food Tours & Gift Certificates.
Image: https://files.boxvault.example/s/a1/PAmexico2018_40.jpg
Body Copy: Feed your curiosity in 17 culinary capitals across the globe
Body copy should be smaller than 15% off food tours and gift certificates (which can be a button or text)

* 1 Graphic promoting 15% off gift certificates.
Image: https://files.boxvault.example/s/a2/Bolo-Rei_009.webp
Body copy: Give them delicious moments they will never forget
Body copy should be smaller than 15% off gift certificates (which can be a button or text)

* Trip-Specific Dark Ads:
* 1 Graphic Ad for each trip:
* Trip 1: Istanbul, September 2025 - Promo Code: ISTJOLLY71 — $200 OFF
Copy: Our week-long Istanbul culinary trips are a feast for your eyes, your stomach, and all your senses. Go beyond baklava with us.
Image: https://files.boxvault.example/s/a3/Harbor-Plates-Shore-20.jpg
* Trip 2: Lisbon, May 2025 - Promo Code: LISJOLLY71 — $200 OFF
Copy: Dig into a buffet of cultures, a bounty of history and all things delicious on our 2025 Lisbon culinary trip. Let us show you the Lisbon that locals love…for less!
Image: https://files.boxvault.example/s/a4/Forno-Dourado.jpg
* Trip 3: Naples, May 2025 - Promo Code: NAPJOLLY71 — $200 OFF
Copy: Expect unexpected moments, unforgettable experiences, and unlimited feasting on our 2025 Naples culinary trip.

Image: https://files.boxvault.example/s/a5/TEODORO-VALLUNGHI_NaplesTour_30.jpg

* Organic Posts
* 1 Graphic Biggest Sale announcement - transparent (will superimpose this graphic over an existing video so copy should not cover the whole screen)
Copy: Dig into our biggest sale of the year!
15% off food tours & gift certificates
$200 off our culinary trips in Lisbon, Naples, and Istanbul
include small logo

* 1 Graphic last chance/end of sale - transparent (will superimpose this graphic over an existing video) . Same style as above sale announcement
Copy: Last chance to dig into delicious deals!
include small logo

2. EMAIL Header Images

* 1 Header Image Sale Announcement

Copy:
We’ve rolled out our biggest sale of the year!
Image: https://files.boxvault.example/s/a6/pa_oaxaca_trip_gallery4.jpg

* 1 Header image Last Chance/End of Sale Reminder
Copy: Last chance to dig into delicious deals
Image: https://files.boxvault.example/s/a7/TEVRI_KUDA_TBILISI_GEORGIA_PA_0360.jpg

Formats and Sizes Needed

Vexo Feed Images:

* Size: 1080 x 1080 pixels
* Aspect Ratio: 1:1
* Format: JPG or PNG
* Max File Size: 30MB

Vexo Story Images:

* Size: 1080 x 1920 pixels
* Aspect Ratio: 9:16
* Format: JPG or PNG

Email Header

* Width: 600–700 pixels (optimal width for most email clients)
* Height: 90–200 pixels (depends on design; typically not too tall to avoid pushing main content too far down)
* Aspect Ratio: 3:1
* Format: JPG or PNG
* File Size: Keep it under 1MB for faster loading times, ideally below 200KB

Deliverable: Trip Specific Dark Ads

Image (choose which looks better in 9:16)
https://files.boxvault.example/s/a8/PA_istanbul_trip_day4.jpg
Or https://files.boxvault.example/s/a9/Harbor-Plates-Shore-20.jpg

Font: Avenir Black 95, Avenir Bold, or Avenir Regular

Logo: All images need vertical or horizontal Pantry Alleyways logo except for Email Header.
https://sheets.papernest.example/doc/7QkLm2Zx9PwR4tVb8Nc

Tagline for 3 trips:
1. September 2025 Istanbul Culinary Trip
Promo Code: ISTJOLLY71 — $200 OFF
COPY: Our week-long Istanbul culinary trip is a feast for your eyes, your stomach, and all your senses. Go beyond baklava with us.
Primary Color
RGB: 181 42 69
CMYK: 22 96 69 10
Hex: #b52a45

2. 2025 Naples Culinary Trip
NAPJOLLY71 — $200 OFF

3. 2025 Lisbon Culinary Trip
Promo Code: LISJOLLY71 — $200 OFF

Tour Deliverable
* 1 Graphic Biggest Sale announcement
* (Last year we used a video - Vexo Organic Post) But we can just request a single image.
* 1 Graphic Last Chance/End of Sale
* (No Example --- New Creative Needed)

Format and size:

Vexo Feed Images:

* Aspect Ratio: 1:1
* Format: JPG or PNG
* Max File Size: 30MB

Vexo Story Images:

* Aspect Ratio: 9:16
* Format: JPG or PNG

NO LOGO FOR EMAIL HEADER!

30 - 65 year olds

tourism and travel

• The photo of man carrying bread, copy, promo code, logo, and font that is listed in the brief under "deliverable"
• other images / graphics besides photo and logo

```html
<!DOCTYPE html>
<html lang="en">
<head>
<meta charset="utf-8">
<title>Pantry Alleyways – Istanbul Culinary Trip Promo</title>
<link rel="stylesheet" href="https://fonts.googleapis.com/css2?family=Outfit:wght@700;800&family=Rajdhani:wght@600&display=swap">
<style>
  :root {
    --brand-red: #b52a45;
    --brand-wine: #8f1c3a;
    --paper: #ffffff;
    --sky: #9fc0d6;
    --bread: #b8793f;
    --shirt: #1f3552;
  }
  html, body {
    margin: 0;
    padding: 0;
    width: 1200px;
    height: 1200px;
    overflow: hidden;
    background: var(--paper);
  }
  .promo {
    position: relative;
    width: 1200px;
    height: 1200px;
    overflow: hidden;
    background: var(--paper);
    font-family: "Outfit", "Avenir", sans-serif;
  }
  .promo__shapes {
    position: absolute;
    inset: 0;
    width: 1200px;
    height: 1200px;
  }
  .band--red { fill: var(--brand-red); }
  .band--wine { fill: var(--brand-wine); }
  .sliver { fill: var(--sky); }

  .brand {
    position: absolute;
    left: 40px;
    top: 230px;
    width: 220px;
    display: flex;
    align-items: center;
    gap: 12px;
  }
  .brand__mark {
    width: 30px;
    height: 30px;
    flex: none;
    background: var(--brand-red);
  }
  .brand__name {
    font-weight: 700;
    font-size: 30px;
    line-height: 1.05;
    color: var(--brand-wine);
  }

  .headline {
    position: absolute;
    left: 287px;
    top: 196px;
    margin: 0;
    color: var(--brand-wine);
    font-weight: 700;
    white-space: nowrap;
  }
  .headline__date {
    display: block;
    font-size: 60px;
    line-height: 66px;
  }
  .headline__title {
    display: block;
    font-size: 62px;
    line-height: 80px;
    letter-spacing: -0.5px;
    text-transform: uppercase;
  }

  .photo {
    position: absolute;
    inset: 0;
    width: 1200px;
    height: 1200px;
  }

  .discount {
    position: absolute;
    left: 23px;
    top: 519px;
    width: 445px;
    height: 132px;
    background: var(--brand-wine);
    color: var(--paper);
    display: flex;
    align-items: center;
    justify-content: center;
    font-weight: 700;
    font-size: 76px;
    line-height: 1;
  }

  .code-badge {
    position: absolute;
    left: 510px;
    top: 420px;
    width: 322px;
    height: 322px;
    border-radius: 50%;
    background: var(--brand-red);
    color: var(--paper);
    display: flex;
    flex-direction: column;
    justify-content: center;
    padding-left: 30px;
    box-sizing: border-box;
    font-weight: 700;
  }
  .code-badge__label { font-size: 39px; line-height: 52px; }
  .code-badge__code { font-size: 39px; line-height: 52px; }

  .body-copy {
    position: absolute;
    left: 25px;
    top: 722px;
    width: 540px;
    margin: 0;
    font-family: "Rajdhani", "Avenir", sans-serif;
    font-weight: 600;
    font-size: 43px;
    line-height: 56.5px;
    color: var(--brand-red);
  }
</style>
</head>
<body>
<main class="promo">
  <svg class="promo__shapes" viewBox="0 0 1600 1600" aria-hidden="true">
    <polygon class="band--red" points="0,0 1600,0 1600,290 330,112 0,282"/>
    <polygon class="band--wine" points="0,0 540,0 0,282"/>
    <polygon class="sliver" points="1060,640 1465,505 1600,482 1600,490 1070,645"/>
    <polygon class="band--red" points="0,1600 195,1458 640,1552 850,1600"/>
    <polygon class="band--wine" points="640,1552 840,1460 850,1600"/>
  </svg>

  <svg class="photo" viewBox="0 0 1600 1600" role="img" aria-label="Photo of a street vendor carrying a large tray of sesame bread rings by the sea">
    <defs>
      <linearGradient id="photoTones" x1="0" y1="0" x2="0" y2="1">
        <stop offset="0" stop-color="#b9d3e4"/>
        <stop offset="0.18" stop-color="#a7c4d8"/>
        <stop offset="0.3" stop-color="#c48a4e"/>
        <stop offset="0.5" stop-color="#a8693a"/>
        <stop offset="0.6" stop-color="#5a3a2a"/>
        <stop offset="0.7" stop-color="#3d6f93"/>
        <stop offset="1" stop-color="#1f3552"/>
      </linearGradient>
    </defs>
    <polygon fill="url(#photoTones)" points="1075,640 1600,495 1600,1600 870,1600 795,990"/>
  </svg>

  <div class="brand">
    <span class="brand__mark"></span>
    <span class="brand__name">Pantry Alleyways</span>
  </div>

  <h1 class="headline">
    <span class="headline__date">September 2025</span>
    <span class="headline__title">Istanbul Culinary Trip</span>
  </h1>

  <div class="discount">$200 OFF</div>

  <div class="code-badge">
    <span class="code-badge__label">Promo Code:</span>
    <span class="code-badge__code">ISTJOLLY71</span>
  </div>

  <p class="body-copy">Our week-long Istanbul culinary trip is a feast for your eyes, your stomach, and all your senses. Go beyond baklava with us.</p>
</main>
</body>
</html>
```